Mox Dune Reel Business cards

Logo, tag line and photo on card
Agent Name
Title
Address
Phone number
Email
Website
Make logo on one side large by rotating  to portrait format.  Keep the background of the logo white.

Contact Information for Business Card
Slogan; Shaping Every Mox Ahead

```html
<!DOCTYPE html>
<html lang="en">
<head>
<meta charset="utf-8">
<title>Mox Dune Reel Business Cards</title>
<link rel="stylesheet" href="https://fonts.googleapis.com/css2?family=Montserrat:wght@500;600;700;800&display=swap">
<style>
  :root {
    --navy: #232f6b;
    --red: #d1262f;
    --white: #ffffff;
    --stage: #a4a5a7;
    --photo-light: #8c8c8c;
    --photo-dark: #3d3d3f;
  }
  * { margin: 0; padding: 0; box-sizing: border-box; }
  html, body { width: 1200px; height: 781px; overflow: hidden; }
  body {
    background: var(--stage);
    font-family: "Montserrat", sans-serif;
    color: var(--navy);
    position: relative;
  }
  .card {
    position: absolute;
    top: 93px;
    width: 340px;
    height: 595px;
    background: var(--white);
    border-radius: 18px;
    overflow: hidden;
    box-shadow: 0 10px 28px rgba(0,0,0,0.28);
  }
  .card--front { left: 230px; }
  .card--back { left: 630px; }
  .card__band {
    position: absolute;
    left: 0; right: 0;
    background: var(--navy);
  }
  .card__footer {
    position: absolute;
    left: 0; right: 0; bottom: 0;
    height: 38px;
    background: var(--red);
  }
  .card__frame {
    position: absolute;
    border: 6px solid var(--red);
    background: var(--white);
    border-radius: 24px;
    overflow: hidden;
  }

  /* Front */
  .card--front .card__band { top: 170px; height: 140px; }
  .agent { position: absolute; top: 46px; left: 0; right: 0; text-align: center; }
  .agent__name { color: var(--red); font-weight: 800; font-size: 24px; letter-spacing: 0.5px; }
  .agent__title { font-weight: 700; font-size: 15px; margin-top: 2px; }
  .card--front .card__frame { top: 112px; left: 45px; width: 250px; height: 238px; }
  .portrait {
    width: 100%; height: 100%;
    background: linear-gradient(180deg, var(--white) 0%, var(--photo-light) 45%, var(--photo-dark) 100%);
  }
  .contact { position: absolute; top: 378px; left: 0; right: 0; text-align: center; font-weight: 500; }
  .contact__address { font-size: 15px; line-height: 1.35; }
  .contact__icons { display: flex; justify-content: center; gap: 8px; margin: 14px 0 12px; }
  .contact__icons svg { width: 14px; height: 14px; }
  .contact__line { font-size: 15px; line-height: 1.4; }
  .contact__phone { letter-spacing: 3px; }

  /* Back */
  .card--back .card__band { top: 190px; height: 150px; }
  .card--back .card__frame {
    top: 135px; left: 38px; width: 264px; height: 260px;
    display: flex; align-items: center; justify-content: center;
  }
  .brand-name {
    font-weight: 800; font-size: 46px; line-height: 1.02;
    color: var(--navy); text-align: center;
  }
  .tagline {
    position: absolute; bottom: 62px; left: 0; right: 0;
    text-align: center; font-weight: 600; font-size: 16px;
  }
</style>
</head>
<body>
  <section class="card card--front">
    <div class="card__band"></div>
    <header class="agent">
      <h1 class="agent__name">CORIN VALE</h1>
      <p class="agent__title">Founder</p>
    </header>
    <div class="card__frame">
      <div class="portrait" role="img" aria-label="Portrait photo of the founder"></div>
    </div>
    <div class="contact">
      <p class="contact__address">Suite 2100, 88 - 5th Avenue<br>SW, Larkfield, AB, T0X 1Z9</p>
      <div class="contact__icons">
        <svg viewBox="0 0 16 16" aria-hidden="true"><circle cx="8" cy="8" r="8" fill="var(--red)"/><path d="M5 4.5l1.6-.4.9 2-1 .8a6 6 0 0 0 2.6 2.6l.8-1 2 .9-.4 1.6c-3.4.2-6.7-3.1-6.5-6.5z" fill="#fff"/></svg>
        <svg viewBox="0 0 16 16" aria-hidden="true"><circle cx="8" cy="8" r="8" fill="var(--red)"/><rect x="3.5" y="5" width="9" height="6.5" rx="1" fill="#fff"/><path d="M3.8 5.3L8 8.6l4.2-3.3" stroke="var(--red)" stroke-width="1" fill="none"/></svg>
        <svg viewBox="0 0 16 16" aria-hidden="true"><circle cx="8" cy="8" r="8" fill="var(--red)"/><path d="M8 3a3 3 0 0 0-3 3c0 2.3 3 6 3 6s3-3.7 3-6a3 3 0 0 0-3-3z" fill="#fff"/><circle cx="8" cy="6" r="1.1" fill="var(--red)"/></svg>
      </div>
      <p class="contact__line contact__phone">555 014 7321</p>
      <p class="contact__line">hello@moxdunereel.com</p>
      <p class="contact__line">www.moxdunereel.com</p>
    </div>
    <div class="card__footer"></div>
  </section>

  <section class="card card--back">
    <div class="card__band"></div>
    <div class="card__frame">
      <p class="brand-name">Mox<br>Dune<br>Reel</p>
    </div>
    <p class="tagline">Shaping Every Mox Ahead</p>
    <div class="card__footer"></div>
  </section>
</body>
</html>
```